Call Center In Need of Website Design

We are a call center that provides inbound and outbound calling & marketing services for eCommerce store. We would like to see a fun, creative, playful design that is simple.

Here are some sample design sites we like;
- https://www.vorlintask.com/
- https://plumdesk.io/
- https://www.tandorix.com/live-chat-software/
- https://www.bexlora.com/

Here are some competitor sites;
- https://www.quillbranchlines.com/
- https://www.helpkestrel.com/

I have attached website content for your use.

Target Market(s)

eCommerce

Coding

Coded - Design and coding required

Number of Pages Required

5+ page

Font styles to use
Sans Serif

Colors

Designer to choose colors to be used in the design.

Requirements
Must have
• Must have designs for the following 5 separate pages;
• 1. Home (landing)
• - This will be were the design style really needs to show.
• - Just needs to touch on key services
• - CTA
• 2. About Us
• - Basic page for about me paragraph
• 3. Services
• - List of services with icons
• - Click on service type to expand details or hover over service icon to view popup bubble with details about that service
• 4. Pricing
• - Option to bundle 1(one) digital service plan and 1(one) call center service plan
• - Bundling adds 10% monthly discount to over all price
• - Customer does NOT have to bundle
• - FAQ
• 5. Contact Us
• - Include a capture form (name, company name, email, phone, message)
• - Contact info
• - Business hours
• When customer purchases their desired plan, then they are taken to a page where they must schedule a call with an account rep.
Nice to have
• home page animations
Should not have
• All information on Home/Landing page.

```html
<!DOCTYPE html>
<html lang="en">
<head>
<meta charset="utf-8">
<title>Veltora — Call Center &amp; Back-Office Support</title>
<link href="https://fonts.googleapis.com/css2?family=Open+Sans:wght@400;600;700&family=Montserrat:wght@400;600&display=swap" rel="stylesheet">
<style>
:root{
  --teal:#6cc7b0;
  --teal-dark:#5ab59e;
  --ink:#3f4a4d;
  --text:#5b6366;
  --muted:#8a9295;
  --line:#e2e6e8;
  --hero-bg:#f7f7f7;
  --faq-bg:#eef3f6;
  --dark:#2f2f2f;
  --field:#222222;
  --btn-dark:#4a5254;
  --white:#ffffff;
}
*{box-sizing:border-box;margin:0;padding:0}
html,body{width:1200px;height:2799px;overflow:hidden}
body{position:relative;background:var(--white);font-family:'Open Sans',Arial,sans-serif;color:var(--text)}
.abs{position:absolute}

/* brand */
.brand{display:flex;align-items:center;gap:14px}
.brand-dot{border:3px solid var(--teal);border-radius:50%}
.brand-name{font-family:'Montserrat',Arial,sans-serif;font-weight:400;color:var(--ink);letter-spacing:4px}

/* header */
.site-header{left:0;top:0;width:1200px;height:90px;background:var(--white)}
.site-header .brand{position:absolute;left:160px;top:24px}
.brand-dot.sm{width:38px;height:38px}
.brand-name.sm{font-size:22px}
.main-nav{position:absolute;left:503px;top:34px;display:flex;gap:26px;font-size:13px;color:var(--ink)}
.main-nav .active{color:var(--teal)}
.btn{display:inline-flex;align-items:center;justify-content:center;font-size:11px;font-weight:600;color:var(--white);border-radius:2px}
.btn-login{position:absolute;left:880px;top:28px;width:75px;height:32px;background:var(--btn-dark)}
.btn-signup{position:absolute;left:963px;top:28px;width:75px;height:32px;background:var(--teal)}

/* hero */
.hero{left:0;top:90px;width:1200px;height:455px;background:var(--hero-bg);overflow:hidden;border-bottom:1px solid var(--line)}
.hero-circle{position:absolute;border-radius:50%;background:#ececec}
.hero .brand{position:absolute;left:160px;top:155px}
.brand-dot.lg{width:56px;height:56px;border-width:4px}
.brand-name.lg{font-size:32px;letter-spacing:6px}
.hero-tagline{position:absolute;left:160px;top:228px;width:360px;font-size:16px;line-height:20px;color:var(--ink)}
.hero .btn{position:absolute;top:280px;height:26px;font-size:8.5px;letter-spacing:.5px}
.btn-start{left:160px;width:80px;background:var(--teal)}
.btn-more{left:252px;width:78px;background:var(--btn-dark)}
.hero-art{position:absolute;left:610px;top:50px;width:405px;height:365px;background:linear-gradient(160deg,#eaf1f5,#c9dbe6 60%,#eef3f6);border-radius:4px}

/* partners */
.partners{left:0;top:545px;width:1200px;height:160px;border-bottom:1px solid var(--line)}
.partners-title{position:absolute;left:160px;top:58px;font-size:14px;font-weight:700;letter-spacing:1px;line-height:18px;color:var(--ink)}
.partners-title span{color:var(--teal)}
.partner-badge{position:absolute;top:38px;width:150px;height:77px;background:#f2f2f2;border:1px solid #dcdcdc}

/* about */
.section-label{display:flex;align-items:center;gap:18px;font-size:11px;font-weight:700;color:var(--ink)}
.section-label::before{content:"";width:50px;height:2px;background:var(--teal)}
.about-label{left:160px;top:731px}
.about-heading{left:160px;top:758px;width:350px;font-size:23px;line-height:32px;font-weight:600;color:var(--ink)}
.about-body{left:535px;top:748px;width:508px;font-size:10.5px;line-height:17px;color:var(--text)}
.about-body p{margin-bottom:14px}
.doodle-art{left:130px;top:862px;width:340px;height:180px;background:radial-gradient(ellipse at center,#eef1f3 0%,rgba(255,255,255,0) 70%)}
.laptop-art{left:0;top:1015px;width:470px;height:315px;background:linear-gradient(180deg,#f3f5f6,#e4e8ea);border-radius:0 8px 8px 0}

/* what we do */
.do-label{left:513px;top:1041px}
.do-heading{left:513px;top:1066px;width:540px;font-size:23px;line-height:31px;font-weight:600;color:var(--ink)}
.do-body{left:513px;top:1146px;width:530px;font-size:10.5px;line-height:17px}
.do-body p{margin-bottom:14px}
.service{position:absolute;top:1262px;display:flex;align-items:center;gap:14px}
.service-icon{width:62px;height:62px;border-radius:50%;background:var(--teal);display:flex;align-items:center;justify-content:center}
.service-name{font-size:23px;line-height:28px;font-weight:600;color:var(--ink)}
.service-digital{left:563px}
.service-call{left:765px}

/* faq */
.faq-wave{left:0;top:1378px;width:1200px;height:30px}
.faq{left:0;top:1406px;width:1200px;height:672px;background:var(--faq-bg)}
.faq-title{position:absolute;left:0;top:56px;width:1200px;text-align:center;font-size:32px;font-weight:600;letter-spacing:1.5px;color:var(--ink)}
.faq-list{position:absolute;left:160px;top:140px;width:880px;list-style:none}
.faq-item{border-bottom:1px solid #d8dfe3;padding:16px 0 15px}
.faq-q{display:flex;justify-content:space-between;font-size:17px;font-weight:600;color:var(--ink);line-height:22px}
.faq-q span:last-child{font-weight:400}
.faq-a{margin-top:12px;font-size:11px;line-height:19px;color:var(--text);width:870px}

/* contact */
.contact{left:0;top:2078px;width:1200px;height:607px;background:var(--dark)}
.contact-title{position:absolute;left:0;top:82px;width:1200px;text-align:center;font-family:'Montserrat',Arial,sans-serif;font-size:24px;font-weight:600;color:var(--white)}
.contact-rule{position:absolute;left:560px;top:127px;width:80px;height:8px}
.contact-intro{position:absolute;left:380px;top:142px;width:440px;text-align:center;font-size:11.5px;line-height:19px;color:#e6e6e6}
.field{position:absolute;background:var(--field);font-size:11px;color:#9a9a9a;padding:12px 10px}
.field-name{left:327px;top:215px;width:260px;height:37px}
.field-email{left:608px;top:215px;width:260px;height:37px}
.field-subject{left:327px;top:269px;width:541px;height:37px}
.field-message{left:327px;top:320px;width:541px;height:150px}
.btn-send{position:absolute;left:532px;top:492px;width:130px;height:37px;background:var(--teal);font-size:10px;letter-spacing:1px}

/* footer */
.site-footer{left:0;top:2685px;width:1200px;height:114px;background:var(--white)}
.site-footer .brand{position:absolute;left:160px;top:33px}
.brand-dot.md{width:46px;height:46px}
.brand-name.md{font-size:26px;letter-spacing:5px}
.footer-divider{position:absolute;left:405px;top:36px;width:1px;height:42px;background:var(--line)}
.copyright{position:absolute;left:425px;top:50px;font-size:10px;color:var(--muted)}
.footer-pin{position:absolute;left:910px;top:36px}
.footer-address{position:absolute;left:948px;top:22px;font-size:10px;line-height:16px;color:var(--text)}
.footer-address strong{color:var(--ink)}
.footer-address .phone{color:var(--teal)}
</style>
</head>
<body>

<header class="site-header abs">
  <div class="brand"><span class="brand-dot sm"></span><span class="brand-name sm">VELTORA</span></div>
  <nav class="main-nav">
    <span class="active">Home</span><span>About Us</span><span>Services</span><span>Pricing</span><span>Contact Us</span>
  </nav>
  <span class="btn btn-login">Login</span>
  <span class="btn btn-signup">Sign Up</span>
</header>

<section class="hero abs">
  <span class="hero-circle" style="left:-40px;top:40px;width:180px;height:180px"></span>
  <span class="hero-circle" style="left:90px;top:10px;width:110px;height:110px;background:#e6e6e6"></span>
  <span class="hero-circle" style="left:80px;top:35px;width:70px;height:70px;background:#dedede"></span>
  <span class="hero-circle" style="left:150px;top:70px;width:150px;height:150px;background:#f0f0f0"></span>
  <div class="brand"><span class="brand-dot lg"></span><span class="brand-name lg">VELTORA</span></div>
  <p class="hero-tagline">Veltora is an omnichannel provider for customer care and back-end office support.</p>
  <span class="btn btn-start">GET STARTED</span>
  <span class="btn btn-more">LEARN MORE</span>
  <div class="hero-art" role="img" aria-label="Isometric illustration of a call center office with agents at desks, captioned call center"></div>
</section>

<section class="partners abs">
  <p class="partners-title"><span>OUR TECHNOLOGY</span><br>PARTNERS</p>
  <div class="partner-badge" style="left:368px"></div>
  <div class="partner-badge" style="left:541px"></div>
  <div class="partner-badge" style="left:714px"></div>
  <div class="partner-badge" style="left:887px"></div>
</section>

<div class="section-label about-label abs">About Us</div>
<h2 class="about-heading abs">Veltora is an omnichannel provider for customer care and back-end office support.</h2>
<div class="about-body abs">
  <p>We primarily work with eCommerce companies around the world. Our service is vital to the core operations and functionality of consumer-focused online eCommerce companies.</p>
  <p>Veltora originally started out as a generalized call center support company. Based in California, the founder quickly realized that there was a lack of support for eCommerce owners that were just getting started. In 2018, Veltora switched gears to offer professional grade call center support at a price that even start-ups could afford.</p>
  <p>Even though Veltora is built to support small business, we are positioned to support medium to enterprise level eCommerce companies. If you are looking to work with a company that is vested in your success, then look no further!</p>
  <p>We look forward to helping your business grow!</p>
</div>
<div class="doodle-art abs" role="img" aria-label="Faint line doodles of office and communication objects"></div>
<div class="laptop-art abs" role="img" aria-label="Laptop showing the home page of the site"></div>

<div class="section-label do-label abs">What We Do</div>
<h2 class="do-heading abs">Veltora is your personal customer service and product research team.</h2>
<div class="do-body abs">
  <p>We love eCommerce, but we love seeing business owners succeed even more! That is exactly why we have developed the processes and technology to take care of the most over looked areas in eCommerce -Customer Service andRetention.</p>
  <p>Let Veltora handle your customers while you focus on growing your business.</p>
</div>
<div class="service service-digital">
  <span class="service-icon"><svg width="30" height="26" viewBox="0 0 30 26" fill="none" stroke="#fff" stroke-width="2"><rect x="2" y="2" width="26" height="17" rx="2"/><path d="M10 24h10M15 19v5"/></svg></span>
  <span class="service-name">Digital<br>Services</span>
</div>
<div class="service service-call">
  <span class="service-icon"><svg width="30" height="30" viewBox="0 0 30 30" fill="none" stroke="#fff" stroke-width="2"><path d="M6 16v-3a9 9 0 0 1 18 0v3"/><rect x="4" y="15" width="5" height="7" rx="2" fill="#fff"/><rect x="21" y="15" width="5" height="7" rx="2" fill="#fff"/><path d="M24 22c0 3-3 5-7 5"/></svg></span>
  <span class="service-name">Call Center<br>Services</span>
</div>

<svg class="faq-wave abs" viewBox="0 0 1200 30" preserveAspectRatio="none" aria-hidden="true">
  <path d="M0 14 Q20 0 40 14 T80 14 T120 14 T160 14 T200 14 T240 14 T280 14 T320 14 T360 14 T400 14 T440 14 T480 14 T520 14 T560 14 T600 14 T640 14 T680 14 T720 14 T760 14 T800 14 T840 14 T880 14 T920 14 T960 14 T1000 14 T1040 14 T1080 14 T1120 14 T1160 14 T1200 14 V30 H0 Z" fill="#eef3f6"/>
</svg>
<section class="faq abs">
  <h2 class="faq-title">FREQUENTLY ASKED QUESTIONS</h2>
  <ul class="faq-list">
    <li class="faq-item">
      <div class="faq-q"><span>Is the free trial really free?</span><span>&minus;</span></div>
      <p class="faq-a">The free trial only relates to the "call center" service packages! There is no hidden fine print or fees to get started. We don't even require any payment info, signatures, or deposits. If you don't like us or our service, just simply walk away.</p>
    </li>
    <li class="faq-item"><div class="faq-q"><span>Do I have to sign a contract?</span><span>+</span></div></li>
    <li class="faq-item"><div class="faq-q"><span>Do I have to purchase any hardware or equipment?</span><span>+</span></div></li>
    <li class="faq-item"><div class="faq-q"><span>Do you offer custom script writing?</span><span>+</span></div></li>
    <li class="faq-item"><div class="faq-q"><span>I'm not sure how many minutes I'll need?</span><span>+</span></div></li>
    <li class="faq-item"><div class="faq-q"><span>Can I change my service plan?</span><span>+</span></div></li>
    <li class="faq-item"><div class="faq-q"><span>Why do you use time-based billing over standard billing?</span><span>+</span></div></li>
    <li class="faq-item"><div class="faq-q"><span>How long does it take to get started?</span><span>+</span></div></li>
  </ul>
</section>

<section class="contact abs">
  <h2 class="contact-title">Get in Touch</h2>
  <svg class="contact-rule" viewBox="0 0 80 8" aria-hidden="true"><path d="M0 4h32M48 4h32" stroke="#aaa" stroke-width="1"/><circle cx="40" cy="4" r="3" fill="none" stroke="#ccc"/></svg>
  <p class="contact-intro">Lorem ipsum dolor sit amet, consectetur adipisicing elit. Asperiores similique dolor ab inventore, veritatis deserunt suscipit vitae minima.</p>
  <div class="field field-name">Your Name</div>
  <div class="field field-email">Your E-Mail</div>
  <div class="field field-subject">Subject</div>
  <div class="field field-message">Your Message</div>
  <span class="btn btn-send">SEND MESSAGE</span>
</section>

<footer class="site-footer abs">
  <div class="brand"><span class="brand-dot md"></span><span class="brand-name md">VELTORA</span></div>
  <span class="footer-divider"></span>
  <p class="copyright">&copy; 2018. All Rights Reserved.</p>
  <svg class="footer-pin" width="18" height="26" viewBox="0 0 18 26" aria-hidden="true"><path d="M9 0a9 9 0 0 0-9 9c0 7 9 17 9 17s9-10 9-17a9 9 0 0 0-9-9z" fill="#4a5254"/><circle cx="9" cy="9" r="3.5" fill="#fff"/></svg>
  <p class="footer-address"><strong>Veltora, Inc.</strong><br>418 Linden Row<br>Marlow Bay, CA 90014<br><span class="phone">(555) 014-2290</span></p>
</footer>

</body>
</html>
```